Property Auctions with Teodor Bramwick

Podcast cover art 3000px by 3000px. Eye catching for a weekly podcast. The words should read Property Auctions (large font) with Teodor Bramwick (smaller font)

I would like the font and colours to be similar to my book, a copy of which I have attached.

Target Market(s)

New and experienced property investors looking to purchase at a property auction

```html
<!DOCTYPE html>
<html lang="en">
<head>
<meta charset="utf-8">
<title>Property Auctions with Teodor Bramwick – Podcast Cover</title>
<link rel="stylesheet" href="https://fonts.googleapis.com/css2?family=Oswald:wght@700&family=Roboto+Condensed:wght@400;700&display=swap">
<style>
  :root {
    --page: #ffffff;
    --navy-dark: #1a1e25;
    --navy-mid: #2e343c;
    --gold-light: #ffe680;
    --gold: #f2b21c;
    --gold-deep: #b8780f;
    --gold-line: #9c7a34;
    --ink: #0b0c0e;
  }
  html, body {
    margin: 0;
    padding: 0;
    width: 1200px;
    height: 1200px;
    overflow: hidden;
    background: var(--page);
  }
  .canvas {
    position: relative;
    width: 1200px;
    height: 1200px;
  }
  .cover {
    position: absolute;
    left: 179px;
    top: 179px;
    width: 842px;
    height: 842px;
    background: radial-gradient(ellipse at 50% 62%, var(--navy-mid) 0%, var(--navy-dark) 75%);
  }
  .artwork {
    position: absolute;
    inset: 0;
    width: 1200px;
    height: 1200px;
  }
  .title {
    font-family: "Oswald", "Arial Narrow", sans-serif;
    font-weight: 700;
    font-size: 158px;
  }
  .with-label {
    font-family: "Roboto Condensed", "Arial Narrow", sans-serif;
    font-weight: 400;
    font-size: 26px;
  }
  .host-name {
    font-family: "Roboto Condensed", "Arial Narrow", sans-serif;
    font-weight: 700;
    font-size: 57px;
  }
</style>
</head>
<body>
<div class="canvas">
  <div class="cover"></div>
  <svg class="artwork" viewBox="0 0 1200 1200" xmlns="http://www.w3.org/2000/svg">
    <defs>
      <linearGradient id="goldText" x1="0" y1="0" x2="0" y2="1">
        <stop offset="0" stop-color="var(--gold-light)"/>
        <stop offset="0.5" stop-color="var(--gold)"/>
        <stop offset="1" stop-color="var(--gold-deep)"/>
      </linearGradient>
      <radialGradient id="goldObject" cx="0.4" cy="0.35" r="0.7">
        <stop offset="0" stop-color="var(--gold-light)"/>
        <stop offset="0.6" stop-color="var(--gold)"/>
        <stop offset="1" stop-color="var(--gold-deep)"/>
      </radialGradient>
      <radialGradient id="houseArea" cx="0.5" cy="0.5" r="0.6">
        <stop offset="0" stop-color="#7a6426"/>
        <stop offset="0.55" stop-color="#3a3320"/>
        <stop offset="1" stop-color="#1f2125"/>
      </radialGradient>
    </defs>

    <!-- Gavel -->
    <rect class="gavel" x="828" y="205" width="172" height="78" rx="30" fill="url(#goldObject)" opacity="0.85" role="img" aria-label="Golden auction gavel"/>

    <!-- Headline -->
    <text class="title" x="304" y="422" textLength="593" lengthAdjust="spacingAndGlyphs" fill="url(#goldText)">PROPERTY</text>
    <text class="title" x="314" y="559" textLength="571" lengthAdjust="spacingAndGlyphs" fill="url(#goldText)">AUCTIONS</text>

    <!-- With divider -->
    <line class="divider" x1="365" y1="586" x2="558" y2="586" stroke="var(--gold-line)" stroke-width="2"/>
    <line class="divider" x1="640" y1="586" x2="835" y2="586" stroke="var(--gold-line)" stroke-width="2"/>
    <text class="with-label" x="600" y="594" text-anchor="middle" fill="var(--gold)">with</text>

    <!-- Host -->
    <text class="host-name" x="371" y="668" textLength="472" lengthAdjust="spacingAndGlyphs" fill="url(#goldText)">TEODOR BRAMWICK</text>

    <!-- Floating pound coins -->
    <rect class="pound" x="345" y="680" width="90" height="102" rx="20" fill="url(#goldObject)" opacity="0.85" role="img" aria-label="Golden pound sign"/>
    <rect class="pound" x="761" y="699" width="64" height="74" rx="16" fill="url(#goldObject)" opacity="0.85" role="img" aria-label="Golden pound sign"/>
    <rect class="pound" x="332" y="876" width="78" height="52" rx="16" fill="url(#goldObject)" opacity="0.85" role="img" aria-label="Golden pound sign"/>
    <rect class="pound" x="774" y="838" width="89" height="134" rx="20" fill="url(#goldObject)" opacity="0.85" role="img" aria-label="Golden pound sign"/>

    <!-- House with rising arrow -->
    <rect class="house-icon" x="440" y="678" width="318" height="294" rx="24" fill="url(#houseArea)" role="img" aria-label="Black and gold house icon with a rising arrow"/>
  </svg>
</div>
</body>
</html>
```